Präsentationsvorlagen / Powerpoint Master for my company
Zielgruppe
Offline hardware device to manage and save passwords safely.
Aufgabenstellung
DIN A4 quer

```html
<!DOCTYPE html>
<html lang="en">
<head>
<meta charset="utf-8">
<title>Keyvane – Presentation Master</title>
<link href="https://fonts.googleapis.com/css2?family=Poppins:ital,wght@0,400;0,500;0,600;0,700;0,800;1,400&display=swap" rel="stylesheet">
<style>
:root{
  --canvas:#a9a9a9;
  --paper:#ffffff;
  --green:#2f7a34;
  --green-dark:#1f5a25;
  --green-soft:#b9dfb1;
  --ink:#1f1f1f;
  --text:#555;
  --muted:#9a9a9a;
  --line:#e2e2e2;
  --bar:#222222;
  --placeholder:#e3e3e3;
}
*{box-sizing:border-box;margin:0;padding:0}
html,body{width:1200px;height:2570px;overflow:hidden;background:var(--canvas)}
body{position:relative;font-family:"Poppins",sans-serif;color:var(--ink)}
.slide{position:absolute;width:553px;height:383px;background:var(--paper);overflow:hidden}
.abs{position:absolute}
.page-no{position:absolute;left:0;top:19px;width:20px;height:12px;background:var(--green);color:#fff;font-size:4px;line-height:12px;text-align:center}
.top-rule{position:absolute;left:32px;top:25px;width:410px;height:1px;background:var(--line)}
.brand{position:absolute;right:20px;top:14px;font-size:17px;font-weight:700;color:var(--green);letter-spacing:.2px}
.footer{position:absolute;left:0;bottom:0;width:100%;height:18px;background:var(--bar)}
.footer .copy{position:absolute;left:20px;top:0;font-size:4.5px;line-height:18px;color:#ddd}
.footer .site{position:absolute;right:0;top:0;width:110px;height:18px;background:var(--green);clip-path:polygon(8px 0,100% 0,100% 100%,0 100%);font-size:4.5px;line-height:18px;color:#fff;text-align:center}
.pill{position:absolute;background:var(--green);color:#fff;font-size:6.5px;font-weight:600;border-radius:9px;padding:0 12px;height:14px;line-height:14px}
.pill-outline{position:absolute;border:1px solid var(--green);color:var(--green);font-size:6.5px;border-radius:9px;height:16px;line-height:14px;padding:0 13px}
.heading{position:absolute;font-size:21px;font-weight:700;line-height:1.22;color:var(--ink)}
.green-rule{position:absolute;width:24px;height:3px;background:var(--green)}
.kicker{position:absolute;font-size:7.5px;font-weight:700;letter-spacing:1px}
.para{position:absolute;font-size:6.5px;line-height:1.95;color:var(--text);text-align:justify}
.photo{position:absolute;background:linear-gradient(160deg,#d8d8d8,#8a8a8a 55%,#3a3a3a)}
.photo.gears{background:linear-gradient(135deg,#bdb7aa,#6b655a 50%,#2c2a26)}
.box{position:absolute;background:var(--placeholder)}
.card{position:absolute;background:#fff;box-shadow:0 3px 14px rgba(0,0,0,.12)}
.mission{position:absolute;width:200px}
.mission .dot{position:absolute;left:0;top:1px;width:9px;height:9px;border-radius:50%;background:var(--green)}
.mission .dot::after{content:"";position:absolute;left:3.3px;top:2.3px;border-left:3.5px solid #fff;border-top:2.2px solid transparent;border-bottom:2.2px solid transparent}
.mission.soft .dot{background:var(--green-soft)}
.mission h4{margin-left:24px;font-size:9px;font-weight:600}
.mission p{margin-left:24px;margin-top:4px;font-size:6px;line-height:1.3;color:var(--text)}
.split-title{position:absolute;font-size:13px;font-weight:600;line-height:1.3}
.split-note{position:absolute;font-size:5.5px;font-style:italic;line-height:1.6;color:var(--text);border-left:1px solid #aaa;padding-left:12px}
.toc-item{position:absolute;left:173px;width:325px}
.toc-item h3{font-size:9.5px;font-weight:500}
.toc-item p{font-size:6px;color:var(--text);margin-top:6px;margin-left:15px;display:flex;align-items:center}
.toc-item p span.rule{flex:1;height:1px;background:var(--line);margin:0 10px}
.toc-item p b{font-weight:500;font-size:6.5px;color:var(--ink);margin-left:8px}
.desc-card{position:absolute;width:229px;height:86px;background:#fff;box-shadow:0 3px 12px rgba(0,0,0,.1)}
.desc-card .box{left:9px;top:7px;width:73px;height:73px}
.desc-card h4{position:absolute;left:95px;top:14px;font-size:9px;font-weight:500;letter-spacing:.3px}
.desc-card p{position:absolute;left:95px;top:32px;width:122px;font-size:6px;line-height:1.55;color:var(--text);text-align:justify}
.price-card{position:absolute;top:123px;width:139px;height:185px;background:#fff;border-radius:6px;box-shadow:0 4px 16px rgba(0,0,0,.13);text-align:center;overflow:hidden}
.price-card .ph{height:28px;background:linear-gradient(#f4f4f4,#cfcfcf);font-size:8px;font-weight:500;line-height:28px}
.price-card .amount{font-size:21px;font-weight:600;margin-top:16px}
.price-card .amount small{font-size:16px;font-weight:500}
.price-card .cash{display:inline-block;margin-top:10px;width:90px;height:18px;border-radius:9px;background:var(--green);color:#fff;font-size:6px;font-weight:600;line-height:18px}
.price-card h5{font-size:6px;font-weight:600;margin-top:10px}
.price-card ul{list-style:disc;text-align:left;margin:10px 0 0 22px;font-size:5.5px;color:var(--text);line-height:1.9}
.step{position:absolute;left:35px;width:270px}
.step .num{position:absolute;left:0;top:0;width:20px;height:20px;border:1.5px solid var(--green);border-radius:50%;font-size:8px;font-weight:600;text-align:center;line-height:17px;color:var(--green);background:#fff}
.step .stem{position:absolute;left:9.5px;top:20px;width:1px;height:20px;background:var(--green)}
.step .stem::after{content:"";position:absolute;left:-2px;bottom:-2px;width:5px;height:5px;border-radius:50%;background:var(--green)}
.step h4{margin-left:38px;font-size:8.5px;font-weight:500}
.step p{margin-left:38px;margin-top:3px;font-size:6px;line-height:1.55;color:var(--text);text-align:justify;width:228px}
.stat{position:absolute;top:295px;font-size:20px;font-weight:600;color:#444}
.stat span{font-size:12px;margin-right:4px}
.stat small{display:block;font-size:7px;font-weight:400;color:var(--text)}
.info-table{position:absolute;left:45px;top:103px;width:463px;border-collapse:collapse;font-size:5px;color:#555;text-align:center}
.info-table th{background:var(--green);color:#fff;font-weight:600;height:22px;font-size:6px}
.info-table td{height:20px}
.info-table tr:nth-child(even) td{background:#e9e9e9}
.info-table tr.sub td{background:#fff;font-weight:600;height:22px;color:#333}
.info-table tr.total td{background:#e9e9e9;font-weight:600;height:22px;color:#333;border-bottom:1px solid #888}
</style>
</head>
<body>

<!-- 1 Cover -->
<section class="slide" style="left:29px;top:47px;background:#1f2b20">
  <div class="photo gears" role="img" aria-label="Machined metal gears on a dark surface" style="left:0;top:0;width:553px;height:365px;background:linear-gradient(110deg,#1d4a22 0%,#2c3a2c 42%,#77705f 70%,#3a3832 100%)"></div>
  <div class="abs" style="left:58px;top:74px;font-size:26px;font-weight:700;color:#fff">Keyvane</div>
  <div class="abs" style="left:56px;top:124px;font-size:39px;font-weight:800;line-height:1.17;color:#fff">BUSINESS<br>PRESENTATION</div>
  <div class="abs" style="left:58px;top:219px;font-size:7px;color:#eee">Lorem ipsum is simply dummy text of the printing and typesetting industry.</div>
  <div class="pill" style="left:60px;top:252px;height:17px;line-height:17px;padding:0 15px">Let's Start</div>
  <div class="footer"><span class="copy">© 2023 All Rights Reserved by keyvane</span><span class="site">www.yourdomain.com</span></div>
</section>

<!-- 2 Contents -->
<section class="slide" style="left:618px;top:47px">
  <div class="page-no">2</div><div class="top-rule"></div><div class="brand">Keyvane</div>
  <div class="abs" style="left:0;top:45px;width:145px;height:320px;background:linear-gradient(90deg,#fff 60%,#efefef)"></div>
  <div class="abs" style="left:72px;top:268px;transform:rotate(-90deg);transform-origin:0 0;white-space:nowrap">
    <span style="font-size:12px;font-weight:600;color:var(--ink)">Table Of </span><span style="font-size:28px;font-weight:600;color:var(--green);letter-spacing:1.5px">CONTENT</span>
  </div>
  <div class="toc-item" style="top:86px"><h3>1.&nbsp; Text Description</h3><p>Lorem Ipsum is simply dummy text<span class="rule"></span><b>01</b></p></div>
  <div class="toc-item" style="top:132px"><h3>2.&nbsp; Text Description</h3><p>Lorem Ipsum is simply dummy text<span class="rule"></span><b>02</b></p></div>
  <div class="toc-item" style="top:179px"><h3>3.&nbsp; Text Description</h3><p>Lorem Ipsum is simply dummy text<span class="rule"></span><b>03</b></p></div>
  <div class="toc-item" style="top:225px"><h3>4.&nbsp; Text Description</h3><p>Lorem Ipsum is simply dummy text<span class="rule"></span><b>04</b></p></div>
  <div class="toc-item" style="top:271px"><h3>5.&nbsp; Text Description</h3><p>Lorem Ipsum is simply dummy text<span class="rule"></span><b>05</b></p></div>
  <div class="footer"><span class="copy">© 2023 All Rights Reserved by keyvane</span><span class="site">www.yourdomain.com</span></div>
</section>

<!-- 3 About -->
<section class="slide" style="left:29px;top:467px">
  <div class="page-no">3</div><div class="top-rule"></div><div class="brand">Keyvane</div>
  <div class="pill" style="left:35px;top:67px">About Us</div>
  <div class="heading" style="left:35px;top:96px">Welcome we are<br>keyvane corporate</div>
  <div class="green-rule" style="left:35px;top:165px"></div>
  <div class="kicker" style="left:35px;top:187px">WE ARE THE BEST COMPANY IN 2023</div>
  <div class="para" style="left:35px;top:210px;width:232px">Lorem ipsum dolor sit amet, consectetur adipiscing elit, sed do eiusmod tempor incididunt ut labore et dolore magna aliqua. Suspendisse potenti nullam ac tortor vitae purus faucibus ornare. Tellus elementum sagittis vitae condimentum id venenatis mattis ullamcorper velit sed faucibus ornare elementum sagittis incididunt ut labore et dolore magna</div>
  <div class="pill-outline" style="left:35px;top:309px">Read More</div>
  <div class="photo" role="img" aria-label="Glass skyscraper seen from below in black and white" style="left:298px;top:65px;width:221px;height:262px;border-radius:10px"></div>
  <div class="footer"><span class="copy">© 2023 All Rights Reserved by keyvane</span><span class="site">www.yourdomain.com</span></div>
</section>

<!-- 4 Mission -->
<section class="slide" style="left:618px;top:467px">
  <div class="page-no">4</div><div class="top-rule"></div><div class="brand">Keyvane</div>
  <div class="pill" style="left:35px;top:67px">About Us</div>
  <div class="heading" style="left:35px;top:96px">Welcome we are<br>keyvane corporate</div>
  <div class="photo" role="img" aria-label="Metal combination lock with letter wheels" style="left:35px;top:167px;width:250px;height:160px;border-radius:8px;background:linear-gradient(120deg,#9a9a9a,#4a4a4a 55%,#1e1e1e)"></div>
  <div class="card" style="left:260px;top:83px;width:251px;height:222px;border-radius:4px"></div>
  <div class="split-title" style="left:280px;top:102px">Our<br>Mission</div>
  <div class="split-note" style="left:346px;top:105px"><b>Lorem Ipsum</b> is simply dummy text<br>of the printing and typesetting industry.</div>
  <div class="mission soft" style="left:282px;top:155px"><span class="dot"></span><h4>Mission One</h4><p>Contrary to popular belief, Lorem Ipsum is not simply random text.</p></div>
  <div class="mission soft" style="left:282px;top:202px"><span class="dot"></span><h4>Mission One</h4><p>Contrary to popular belief, Lorem Ipsum is not simply random text.</p></div>
  <div class="mission soft" style="left:282px;top:252px"><span class="dot"></span><h4>Mission One</h4><p>Contrary to popular belief, Lorem Ipsum is not simply random text.</p></div>
  <div class="footer"><span class="copy">© 2023 All Rights Reserved by keyvane</span><span class="site">www.yourdomain.com</span></div>
</section>

<!-- 5 Vision -->
<section class="slide" style="left:29px;top:886px">
  <div class="page-no">5</div><div class="top-rule" style="width:245px"></div>
  <div class="pill" style="left:35px;top:67px">About Us</div>
  <div class="split-title" style="left:38px;top:109px">Our<br>Vision</div>
  <div class="split-note" style="left:103px;top:113px"><b>Lorem Ipsum</b> is simply dummy text<br>of the printing and typesetting industry.</div>
  <div class="mission" style="left:40px;top:162px"><span class="dot"></span><h4>Mission One</h4><p>Contrary to popular belief, Lorem Ipsum is not simply random text.</p></div>
  <div class="mission" style="left:40px;top:209px"><span class="dot"></span><h4>Mission One</h4><p>Contrary to popular belief, Lorem Ipsum is not simply random text.</p></div>
  <div class="mission" style="left:40px;top:259px"><span class="dot"></span><h4>Mission One</h4><p>Contrary to popular belief, Lorem Ipsum is not simply random text.</p></div>
  <div class="photo" role="img" aria-label="Glass skyscraper seen from below in black and white" style="left:298px;top:0;width:255px;height:296px"></div>
  <div class="footer"><span class="copy">© 2023 All Rights Reserved by keyvane</span><span class="site">www.yourdomain.com</span></div>
</section>

<!-- 6 Service -->
<section class="slide" style="left:618px;top:886px">
  <div class="page-no">6</div><div class="top-rule"></div><div class="brand">Keyvane</div>
  <div class="pill" style="left:35px;top:67px">About Us</div>
  <div class="heading" style="left:35px;top:96px">We provide you<br>with best service</div>
  <div class="green-rule" style="left:35px;top:165px"></div>
  <div class="kicker" style="left:35px;top:187px">WE ARE THE BEST COMPANY IN 2023</div>
  <div class="para" style="left:35px;top:210px;width:191px">Lorem ipsum dolor sit amet, consectetur adipiscing elit, sed do eiusmod tempor incididunt ut labore et dolore magna aliqua. Suspendisse potenti nullam ac tortor vitae purus faucibus ornare. Tellus elementum sagittis vitae condimentum id venenatis mattis ullamcorper velit sed faucibus ornare elementum sagittis incididunt ut labore et dolore magna</div>
  <div class="card" style="left:268px;top:62px;width:245px;height:183px"></div>
  <div class="photo gears" role="img" aria-label="Stacked metal gears" style="left:277px;top:70px;width:227px;height:115px"></div>
  <div class="abs" style="left:287px;top:202px;font-size:7.5px;font-weight:600">THIS IS YOUR DESCRIPTION TEXT</div>
  <div class="abs" style="left:287px;top:218px;width:212px;font-size:5.5px;line-height:1.7;color:var(--muted)">Sed ut perspiciatis unde omnis iste natus error sit voluptatem accusantium doloremque laudantium.</div>
  <div class="card" style="left:268px;top:260px;width:122px;height:60px;border-left:3px solid var(--green)"></div>
  <div class="card" style="left:393px;top:260px;width:120px;height:60px"></div>
  <div class="abs" style="left:284px;top:268px;font-size:18px;font-weight:600;color:var(--green)">45</div>
  <div class="abs" style="left:316px;top:275px;font-size:5.5px;font-weight:600">TITLE TEXT ONE</div>
  <div class="abs" style="left:284px;top:292px;font-size:5.5px;line-height:1.6;color:var(--muted)">Sed ut perspiciatis unde<br>omnis iste natus.</div>
  <div class="abs" style="left:403px;top:268px;font-size:18px;font-weight:600;color:var(--green)">85</div>
  <div class="abs" style="left:435px;top:275px;font-size:5.5px;font-weight:600">TITLE TEXT TWO</div>
  <div class="abs" style="left:403px;top:292px;font-size:5.5px;line-height:1.6;color:var(--muted)">Sed ut perspiciatis unde<br>omnis iste natus.</div>
  <div class="footer"><span class="copy">© 2023 All Rights Reserved by keyvane</span><span class="site">www.yourdomain.com</span></div>
</section>

<!-- 7 Descriptions -->
<section class="slide" style="left:29px;top:1305px">
  <div class="page-no">7</div><div class="top-rule"></div><div class="brand">Keyvane</div>
  <div class="abs" style="left:35px;top:78px;font-size:16px;font-weight:600">Title <span style="color:var(--green)">Text</span></div>
  <div class="green-rule" style="left:35px;top:113px"></div>
  <div class="desc-card" style="left:35px;top:130px"><div class="box"></div><h4>DESCRIPTION</h4><p><b>Lorem Ipsum</b> is simply dummy text of the printing and typesetting industry. The industry's standard dummy text ever since the 1500s.</p></div>
  <div class="desc-card" style="left:281px;top:130px"><div class="box"></div><h4>DESCRIPTION</h4><p><b>Lorem Ipsum</b> is simply dummy text of the printing and typesetting industry. The industry's standard dummy text ever since the 1500s.</p></div>
  <div class="desc-card" style="left:35px;top:230px"><div class="box"></div><h4>DESCRIPTION</h4><p><b>Lorem Ipsum</b> is simply dummy text of the printing and typesetting industry. The industry's standard dummy text ever since the 1500s.</p></div>
  <div class="desc-card" style="left:281px;top:230px"><div class="box"></div><h4>DESCRIPTION</h4><p><b>Lorem Ipsum</b> is simply dummy text of the printing and typesetting industry. The industry's standard dummy text ever since the 1500s.</p></div>
  <div class="footer"><span class="copy">© 2023 All Rights Reserved by keyvane</span><span class="site">www.yourdomain.com</span></div>
</section>

<!-- 8 Products -->
<section class="slide" style="left:618px;top:1305px">
  <div class="page-no">8</div><div class="top-rule"></div><div class="brand">Keyvane</div>
  <div class="pill" style="left:35px;top:67px">About Us</div>
  <div class="heading" style="left:35px;top:96px">We provide you<br>best service</div>
  <div class="green-rule" style="left:35px;top:165px"></div>
  <div class="kicker" style="left:35px;top:187px">WE ARE THE BEST COMPANY IN 2023</div>
  <div class="para" style="left:35px;top:210px;width:191px">Lorem ipsum dolor sit amet, consectetur adipiscing elit, sed do eiusmod tempor incididunt ut labore et dolore magna aliqua. Suspendisse potenti nullam ac tortor vitae purus faucibus ornare. Tellus elementum sagittis vitae magna condimentum id venenatis mattis ullamcorper velit sed faucibus labore et dolore.</div>
  <div class="pill-outline" style="left:35px;top:299px">Read More</div>
  <div class="box" style="left:256px;top:66px;width:118px;height:182px"></div>
  <div class="box" style="left:387px;top:66px;width:118px;height:182px"></div>
  <div class="abs" style="left:256px;top:262px;width:118px;text-align:center">
    <div style="font-size:8px;font-weight:600;color:var(--green)">Product One</div>
    <div style="font-size:6px;line-height:1.5;color:var(--muted);margin-top:3px">A wonderful serenity has<br>taken possession</div>
    <div style="font-size:13px;font-weight:600;color:var(--green);margin-top:3px">$230.3</div>
  </div>
  <div class="abs" style="left:387px;top:261px;width:118px;text-align:center">
    <div style="font-size:8px;font-weight:600;color:var(--green)">Product Two</div>
    <div style="font-size:6px;line-height:1.5;color:var(--muted);margin-top:3px">A wonderful serenity has<br>taken possession</div>
    <div style="font-size:13px;font-weight:600;color:var(--green);margin-top:3px">$333.3</div>
  </div>
  <div class="footer"><span class="copy">© 2023 All Rights Reserved by keyvane</span><span class="site">www.yourdomain.com</span></div>
</section>

<!-- 9 Pricing -->
<section class="slide" style="left:30px;top:1725px;width:555px;background:#f1f1f1">
  <div class="page-no">9</div><div class="top-rule"></div><div class="brand">Keyvane</div>
  <div class="abs" style="left:0;top:56px;width:100%;text-align:center;font-size:18px;font-weight:600">Pricing Table</div>
  <div class="price-card" style="left:48px"><div class="ph">Package 01</div><div class="amount">$39<small>/mo</small></div><span class="cash">10% Cashback</span><h5>Services</h5><ul><li>Lorem ipsum dolor sit amet,</li><li>consectetur adipiscing elit.</li><li>Pellentesque scel malesuada</li></ul></div>
  <div class="price-card" style="left:208px"><div class="ph">Package 02</div><div class="amount">$59<small>/mo</small></div><span class="cash">20% Cashback</span><h5>Services</h5><ul><li>Lorem ipsum dolor sit amet,</li><li>consectetur adipiscing elit.</li><li>Pellentesque scel malesuada</li></ul></div>
  <div class="price-card" style="left:368px"><div class="ph">Package 03</div><div class="amount">$89<small>/mo</small></div><span class="cash">30% Cashback</span><h5>Services</h5><ul><li>Lorem ipsum dolor sit amet,</li><li>consectetur adipiscing elit.</li><li>Pellentesque scel malesuada</li></ul></div>
  <div class="footer"><span class="copy">© 2023 All Rights Reserved by keyvane</span><span class="site">www.yourdomain.com</span></div>
</section>

<!-- 10 Steps -->
<section class="slide" style="left:618px;top:1725px;width:555px">
  <div class="page-no">10</div><div class="top-rule"></div><div class="brand">Keyvane</div>
  <div class="step" style="top:77px"><span class="num">01</span><span class="stem"></span><h4>TITLE TEXT HERE</h4><p><b>Lorem Ipsum</b> is simply dummy text of the printing and typesetting industry. Lorem Ipsum has been the industry's standard dummy text ever since the 1500s.</p></div>
  <div class="step" style="top:139px"><span class="num">02</span><span class="stem"></span><h4>TITLE TEXT HERE</h4><p><b>Lorem Ipsum</b> is simply dummy text of the printing and typesetting industry. Lorem Ipsum has been the industry's standard dummy text ever since the 1500s.</p></div>
  <div class="step" style="top:201px"><span class="num">03</span><span class="stem"></span><h4>TITLE TEXT HERE</h4><p><b>Lorem Ipsum</b> is simply dummy text of the printing and typesetting industry. Lorem Ipsum has been the industry's standard dummy text ever since the 1500s.</p></div>
  <div class="step" style="top:263px"><span class="num">04</span><span class="stem"></span><h4>TITLE TEXT HERE</h4><p><b>Lorem Ipsum</b> is simply dummy text of the printing and typesetting industry. Lorem Ipsum has been the industry's standard dummy text ever since the 1500s.</p></div>
  <div class="photo gears" role="img" aria-label="Close-up of interlocking metal gears" style="left:328px;top:62px;width:192px;height:258px;border-radius:6px"></div>
  <div class="footer"><span class="copy">© 2023 All Rights Reserved by keyvane</span><span class="site">www.yourdomain.com</span></div>
</section>

<!-- 11 Chart -->
<section class="slide" style="left:32px;top:2145px">
  <div class="page-no">11</div><div class="top-rule"></div><div class="brand">Keyvane</div>
  <div class="abs" style="left:0;top:73px;width:553px;text-align:center;font-size:18px;font-weight:600">Chart Infographic</div>
  <svg class="abs" style="left:0;top:110px" width="553" height="170" viewBox="0 0 553 170" font-family="Poppins,sans-serif" font-size="6" fill="#666">
    <g font-size="5.5"><rect x="222" y="8" width="4" height="4" fill="#7a7a7a"/><text x="228" y="12">Series 1</text>
    <rect x="262" y="8" width="4" height="4" fill="#2f7a34"/><text x="268" y="12">Series 2</text>
    <rect x="302" y="8" width="4" height="4" fill="#b9dfb1"/><text x="308" y="12">Series 3</text></g>
    <g stroke="#e6e6e6" stroke-width="1">
      <line x1="50" y1="25" x2="510" y2="25"/><line x1="50" y1="46" x2="510" y2="46"/><line x1="50" y1="67" x2="510" y2="67"/>
      <line x1="50" y1="88" x2="510" y2="88"/><line x1="50" y1="109" x2="510" y2="109"/><line x1="50" y1="130" x2="510" y2="130"/>
      <line x1="50" y1="151" x2="510" y2="151" stroke="#ccc"/></g>
    <g text-anchor="end"><text x="44" y="27">6</text><text x="44" y="48">5</text><text x="44" y="69">4</text><text x="44" y="90">3</text><text x="44" y="111">2</text><text x="44" y="132">1</text><text x="44" y="153">0</text></g>
    <rect x="74" y="60" width="20" height="91" fill="#7a7a7a"/><rect x="99" y="101" width="20" height="50" fill="#2f7a34"/><rect x="124" y="109" width="20" height="42" fill="#b9dfb1"/>
    <rect x="188" y="98" width="20" height="53" fill="#7a7a7a"/><rect x="213" y="58" width="20" height="93" fill="#2f7a34"/><rect x="238" y="109" width="20" height="42" fill="#b9dfb1"/>
    <rect x="302" y="77" width="20" height="74" fill="#7a7a7a"/><rect x="327" y="113" width="20" height="38" fill="#2f7a34"/><rect x="352" y="88" width="20" height="63" fill="#b9dfb1"/>
    <rect x="417" y="56" width="20" height="95" fill="#7a7a7a"/><rect x="442" y="92" width="20" height="59" fill="#2f7a34"/><rect x="467" y="46" width="20" height="105" fill="#b9dfb1"/>
    <g text-anchor="middle"><text x="109" y="163">Category 1</text><text x="223" y="163">Category 2</text><text x="337" y="163">Category 3</text><text x="452" y="163">Category 4</text></g>
  </svg>
  <div class="stat" style="left:52px"><span style="color:#888">▲</span>45%<small>Insert Your Text</small></div>
  <div class="stat" style="left:146px"><span style="color:var(--green)">▼</span>45%<small>Insert Your Text</small></div>
  <div class="stat" style="left:240px"><span style="color:var(--green-soft)">▲</span>45%<small>Insert Your Text</small></div>
  <div class="abs" style="left:340px;top:298px;width:150px;font-size:6.5px;line-height:1.6;color:var(--text)">Lorem ipsum dolor sit amet, consectetur adipiscing elit. Integer nec odio. Praesent libero.</div>
  <div class="footer"><span class="copy">© 2023 All Rights Reserved by keyvane</span><span class="site">www.yourdomain.com</span></div>
</section>

<!-- 12 Table -->
<section class="slide" style="left:618px;top:2145px">
  <div class="page-no">12</div><div class="top-rule"></div><div class="brand">Keyvane</div>
  <div class="abs" style="left:0;top:62px;width:553px;text-align:center;font-size:18px;font-weight:600">Table Infographic</div>
  <table class="info-table">
    <tr><th>Column</th><th>Col 1</th><th>Col 2</th><th>Col 3</th><th>Col 4</th><th>Desc.</th></tr>
    <tr><td>Sample text</td><td>-</td><td>123.456</td><td>-</td><td>123.456</td><td>-</td></tr>
    <tr><td>Insert text here</td><td>123.456</td><td>-</td><td>123.456</td><td>-</td><td>123.456</td></tr>
    <tr><td>Dummy text</td><td>-</td><td>123.456</td><td>-</td><td>123.456</td><td>-</td></tr>
    <tr><td>Example text</td><td>123.456</td><td>-</td><td>123.456</td><td>-</td><td>123.456</td></tr>
    <tr><td>Sample text</td><td>-</td><td>123.456</td><td>-</td><td>123.456</td><td>-</td></tr>
    <tr><td>Simply text</td><td>123.456</td><td>-</td><td>123.456</td><td>-</td><td>123.456</td></tr>
    <tr><td>Insert here</td><td>-</td><td>123.456</td><td>-</td><td>123.456</td><td>-</td></tr>
    <tr class="sub"><td>Sub Total</td><td>123.456</td><td>123.456</td><td>123.456</td><td>123.456</td><td>123.456</td></tr>
    <tr class="total"><td>Total</td><td>123.456</td><td>123.456</td><td>123.456</td><td>123.456</td><td>123.456</td></tr>
  </table>
  <div class="abs" style="left:46px;top:328px;font-size:4.5px;font-style:italic;color:var(--text)">* Lorem ipsum dolor sit amet, consectetur adipiscing elit. Phasellus id nisi vitae leo convallis porta.</div>
  <div class="footer"><span class="copy">© 2023 All Rights Reserved by keyvane</span><span class="site">www.yourdomain.com</span></div>
</section>

</body>
</html>
```